BrivoMatex. Lantern for the Steady Growth. Business card

Professional business card for BrivoMatex (Lantern for the Steady Growth)
My rationale: Strategy-> Execution-> Results-> Value that lead to the BrivoMatex name: We put the Lantern for the Steady Growth.
We deliver value to our customers helping them at defining a good strategy (cyan arrow). 90% of well formulated strategies fail due to poor execution so we also consider strategical execution very important (green arrow). Due to the execution we obtain the results (blue arrow). Finally, the results provide feedback to redefine strategy, and the new strategy has to be executed and new results obtained providing new feedback and on and on. It's like a wheel that finally, must create corporate value: value for shareholders, staholders, employees, providers...-

Target Market(s)

CEOs and steering comitees , invewrnent funds

Industry/Entity Type

Business Consultant

Contact Information for Business Card

Tommaso Ferlini
CEO & Founder
tommaso.ferlini@brivomatex.example
Mobile: +34 611.205.938
www.brivomatex.example

Colors

Designer to choose colors to be used in the design.

Requirements
Nice to have
• Nice to hace the words: Strategy, execution, results
• Nice to vave the claim: Lantern for the Steady Growth
• The three colors should be shown:
• cyan for STRATEGY
• green for EXECUTION
• blue for RESULTS
Should not have
• Complete black background

```html
<!DOCTYPE html>
<html lang="en">
<head>
<meta charset="utf-8">
<title>BrivoMatex — Business Card</title>
<link rel="stylesheet" href="https://fonts.googleapis.com/css2?family=Open+Sans:wght@400;600;700&display=swap">
<style>
  :root {
    --brand-blue: #223f94;
    --brand-green: #8cc63f;
    --brand-cyan: #29abe2;
    --ink: #3a3a3a;
    --paper: #ffffff;
    --backdrop: #e9e8e6;
  }
  * { box-sizing: border-box; margin: 0; padding: 0; }
  html, body {
    width: 1200px;
    height: 716px;
    overflow: hidden;
    background: var(--backdrop);
    font-family: "Open Sans", Arial, sans-serif;
  }
  .sheet {
    width: 1200px;
    height: 716px;
    display: flex;
    align-items: center;
    justify-content: center;
    gap: 40px;
  }
  .card {
    position: relative;
    width: 540px;
    height: 309px;
    border-radius: 2px;
    overflow: hidden;
    box-shadow: 0 6px 18px rgba(0,0,0,0.18);
  }

  /* Front */
  .card--front {
    background: var(--brand-blue);
    display: flex;
    align-items: center;
    justify-content: center;
  }
  .wordmark {
    font-weight: 700;
    letter-spacing: -0.02em;
    line-height: 1;
  }
  .card--front .wordmark {
    color: var(--paper);
    font-size: 52px;
  }

  /* Back */
  .card--back { background: var(--paper); }
  .back-wave {
    position: absolute;
    inset: 0;
    width: 100%;
    height: 100%;
  }
  .back-brand {
    position: absolute;
    left: 40px;
    top: 112px;
    width: 210px;
    text-align: center;
  }
  .card--back .wordmark {
    color: var(--brand-blue);
    font-size: 34px;
  }
  .divider {
    position: absolute;
    left: 262px;
    top: 92px;
    width: 1.5px;
    height: 96px;
    background: var(--brand-green);
  }
  .contact {
    position: absolute;
    left: 280px;
    top: 92px;
    color: var(--ink);
  }
  .contact__name {
    font-size: 18px;
    font-weight: 700;
    line-height: 1.1;
  }
  .contact__first { color: var(--brand-green); }
  .contact__last { color: var(--brand-blue); }
  .contact__title {
    font-size: 11px;
    margin: 3px 0 8px;
  }
  .contact__list { list-style: none; }
  .contact__item {
    display: flex;
    align-items: center;
    gap: 6px;
    font-size: 11.5px;
    line-height: 1.55;
  }
  .contact__icon {
    width: 10px;
    height: 10px;
    flex: none;
    fill: var(--brand-blue);
  }
</style>
</head>
<body>
<main class="sheet">
  <section class="card card--front" aria-label="Card front">
    <span class="wordmark">BrivoMatex</span>
  </section>

  <section class="card card--back" aria-label="Card back">
    <svg class="back-wave" viewBox="0 0 540 309" preserveAspectRatio="none" aria-hidden="true">
      <path d="M0,186 C120,250 260,250 400,272 C460,281 510,286 540,296 L540,309 L0,309 Z" fill="var(--brand-blue)"/>
      <path d="M0,178 C120,244 260,244 400,266 C460,275 510,281 540,290" fill="none" stroke="var(--brand-green)" stroke-width="3"/>
      <path d="M0,168 C110,234 260,236 400,258 C460,267 510,273 540,283" fill="none" stroke="var(--brand-cyan)" stroke-width="3"/>
    </svg>

    <div class="back-brand">
      <span class="wordmark">BrivoMatex</span>
    </div>

    <div class="divider"></div>

    <div class="contact">
      <p class="contact__name"><span class="contact__first">Tommaso</span> <span class="contact__last">Ferlini</span></p>
      <p class="contact__title">CEO &amp; Founder</p>
      <ul class="contact__list">
        <li class="contact__item">
          <svg class="contact__icon" viewBox="0 0 10 10" aria-hidden="true"><path d="M2.5 0h5a1 1 0 0 1 1 1v8a1 1 0 0 1-1 1h-5a1 1 0 0 1-1-1V1a1 1 0 0 1 1-1zm.3 1.2v6.4h4.4V1.2zM5 8.3a.5.5 0 1 0 0 1 .5.5 0 0 0 0-1z"/></svg>
          +34 611.205.938
        </li>
        <li class="contact__item">
          <svg class="contact__icon" viewBox="0 0 10 10" aria-hidden="true"><path d="M0 2h10v6H0zM0.6 2.4 5 5.6l4.4-3.2v.9L5 6.5.6 3.3z" fill-rule="evenodd"/></svg>
          tommaso.ferlini@brivomatex.example
        </li>
        <li class="contact__item">
          <svg class="contact__icon" viewBox="0 0 10 10" aria-hidden="true"><circle cx="5" cy="5" r="4.6"/><path d="M3 2.5c1 .3 1.5 1 1 1.8-.4.6.4 1.2 1 1 .8-.2 1 .8.4 1.6-.4.5-.2 1.3.3 1.6M6.5 1.4c-.3.8.3 1.3 1 1.2" fill="none" stroke="#fff" stroke-width=".7"/></svg>
          www.brivomatex.example
        </li>
      </ul>
    </div>
  </section>
</main>
</body>
</html>
```